Mango Grove Indian Restaurants 2019 Menu

Hi,
Please find attached menu text in pdf format. It contains 4 pages. Please work on the menu pages. I will further work with the winner to add the cover page and images as an extended project

Please visit www.mangogroveeats.com.au for more information

```html
<!DOCTYPE html>
<html lang="en">
<head>
<meta charset="utf-8">
<title>Mango Grove Indian Restaurants – Menu</title>
<link href="https://fonts.googleapis.com/css2?family=PT+Sans+Narrow:wght@400;700&display=swap" rel="stylesheet">
<style>
:root{
  --backdrop:#d4d4d4;
  --paper:#ffffff;
  --ink:#3a3a3a;
  --ink-soft:#5a5a5a;
  --red:#c8161d;
  --red-dark:#a51016;
  --gold:#e8b12a;
  --leaf:#6fae3a;
  --mist:#ececec;
}
*{box-sizing:border-box;margin:0;padding:0}
html,body{width:800px;height:1200px;overflow:hidden;background:var(--backdrop)}
body{font-family:"PT Sans Narrow",sans-serif;color:var(--ink)}
.stage{position:absolute;left:0;top:0;width:1000px;height:1500px;transform:scale(.8);transform-origin:0 0}
.page{position:absolute;left:281px;width:421px;height:596px;background:var(--paper);overflow:hidden}
.page--starters{top:116px}
.page--curries{top:792px}
.page-header{position:absolute;left:0;top:0;width:100%;height:70px;
  background:linear-gradient(180deg,#e2e2e2 0%,#f3f3f3 60%,#fff 100%)}
.header-garnish{position:absolute;right:0;top:0;width:140px;height:60px;
  background:radial-gradient(ellipse at 70% 40%,#f4f1ea 0%,#d9d4cb 45%,transparent 75%),
  radial-gradient(ellipse at 20% 10%,#c23a2a 0%,transparent 45%)}
.brand{position:absolute;left:140px;top:22px;width:140px;text-align:center}
.brand-name{display:block;font-weight:700;font-size:19px;color:var(--red);line-height:1}
.brand-sub{display:block;margin:2px auto 0;width:70px;background:var(--red);color:#fff;font-size:4.5px;letter-spacing:.4px;line-height:7px}
.section-tag{position:absolute;left:18px;height:16px;padding:0 12px;background:var(--red);color:#fff;
  font-size:8px;line-height:16px;transform:skewX(-12deg)}
.section-tag span{display:inline-block;transform:skewX(12deg)}
.col{position:absolute;display:flex;flex-direction:column;gap:7px}
.item-head{display:flex;align-items:center;gap:4px;font-size:5px;color:var(--ink)}
.item-head .price{margin-left:auto;font-weight:700;font-size:6px}
.spice{display:inline-flex;align-items:center;gap:2px;color:var(--red);font-size:4.5px}
.spice::before{content:"";width:8px;height:2px;border-radius:0 2px 2px 0;background:var(--red);transform:rotate(-8deg)}
.veg{width:5px;height:5px;border-radius:50%;border:1px solid var(--leaf)}
.desc{font-size:4px;line-height:1.45;color:var(--ink-soft);margin-top:1px}
.rows{display:grid;grid-template-columns:1fr auto;font-size:4px;color:var(--ink-soft);line-height:1.5}
.rows b{font-size:6px;color:var(--ink);text-align:right}
.photo{position:absolute;border:1px solid #999}
.band-title{position:absolute;left:220px;top:372px;width:184px;height:16px;background:var(--red);color:#fff;
  font-size:7px;line-height:16px;padding-left:10px;transform:skewX(-8deg)}
.page-foot{position:absolute;left:0;bottom:0;width:100%;height:14px;
  background:linear-gradient(180deg,var(--gold) 0 3px,#fff 3px 5px,var(--red) 5px 100%)}
.price-line{position:absolute;left:78px;top:79px;font-size:6px;color:var(--ink)}
.curry-list{gap:6px}
</style>
</head>
<body>
<div class="stage">

  <section class="page page--starters">
    <div class="page-header"><div class="header-garnish" role="img" aria-label="Red chillies and a bowl of rice"></div></div>
    <div class="brand"><span class="brand-name">Mango Grove</span><span class="brand-sub">INDIAN RESTAURANT</span></div>
    <div class="section-tag" style="top:37px"><span>STARTERS</span></div>

    <div class="col" style="left:17px;top:62px;width:183px">
      <div>
        <div class="item-head">65 (8 PCS) , DF, NF <span class="spice">MODERATE</span></div>
        <div class="rows"><span>Gobi (Cauliflower)</span><b>$8</b><span>Chicken</span><b>$14</b></div>
        <p class="desc">Extra per piece Gobi (Cauliflower) $1 | Chicken $1.5<br>Boneless chicken or gobi pieces marinated in a home-made special masala mix and deep fried in spicy batter made with chickpea flour and exotic spices.</p>
      </div>
      <div>
        <div class="item-head">Palak Pakora Chat (8pcs) DF,GF, NF <span class="spice">MILD</span><i class="veg"></i><span class="price">$12</span></div>
        <p class="desc">Extra per piece $1.50<br>Crispy fried spinach leaves dipped in mildly spiced chickpea batter topped with tangy chutneys, yoghurt, onion, tomato finished with sprinkles of mildly spiced crunchy chickpea noodles.</p>
      </div>
      <div>
        <div class="item-head">Chilli Dry (8 pcs) DF,GF, NF <span class="spice">HOT</span><i class="veg"></i><span class="price">$12</span></div>
        <p class="desc">Extra per piece $1.5<br>Mushroom/Paneer (cheese) /Chicken $14 extra per piece $1.5 Fish/Prawn $20 Extra per piece $2.5<br>Battered and fried vegetables/meats/seafood smothered in home-made sauce made with a variety of chillies, celery, cabbage, ginger, garlic, soy sauce, vinegar and exotic spices. Gobi (Cauliflower)</p>
      </div>
      <div>
        <div class="item-head">Potato Fries DF,GF, NF <i class="veg"></i></div>
        <p class="desc">Thin cut straight deep fried local potatoes. Small $5 | Large $8</p>
      </div>
    </div>

    <div class="photo" style="left:18px;top:279px;width:181px;height:95px;background:radial-gradient(ellipse at 50% 50%,#7a2a18 0%,#9b3a1e 40%,#cfc7bd 80%)" role="img" aria-label="Plate of chilli fried starter"></div>

    <div class="col" style="left:17px;top:392px;width:183px">
      <div>
        <div class="item-head">Samosa (2 pcs) NF <span class="spice">MODERATE</span></div>
        <div class="rows"><span>Vegetable</span><b>$6</b><span>Chicken</span><b>$7</b><span>Lamb</span><b>$8</b></div>
        <p class="desc">Extra per piece Vegetable $3 | Chicken $3.5 | Lamb $4<br>Deep fried, triangular, savoury pastry containing mildly spiced vegetables or meat filling. Standard serving contains 2 large pieces.</p>
      </div>
      <div>
        <div class="item-head">Samosa Chat (3pcs) NF <span class="spice">MODERATE</span> <span style="margin-left:14px;font-size:4px">Extra per piece $4</span><span class="price">$12</span></div>
        <p class="desc">Crushed vegetable samosa pieces topped with tangy chutneys, yoghurt, onion, tomato finished with sprinkles of mildly spiced crunchy chickpea noodles.</p>
      </div>
      <div>
        <div class="item-head">Manchurian Dry (8 pcs) DF,GF, NF <span class="spice">HOT</span><i class="veg"></i></div>
        <div class="rows" style="grid-template-columns:1fr 1fr auto"><span>Gobi (Cauliflower)</span><span>Extra per piece $1.5</span><b>$12</b><span>Mushroom/Paneer (cheese) /Chicken</span><span>Extra per piece $1.5</span><b>$14</b><span>Fish/Prawn</span><span>Extra per piece $2.5</span><b>$20</b></div>
        <p class="desc">Battered and fried vegetables/meats/seafood that are tossed in home-made sauce made with celery, cabbage, ginger, garlic, soy sauce, vinegar and exotic spices.</p>
      </div>
    </div>

    <div class="photo" style="left:220px;top:63px;width:184px;height:81px;background:linear-gradient(90deg,#b07a3a,#d9a860 30%,#8a5a2a 55%,#d7a55c 80%,#a8743a)" role="img" aria-label="Fried kebab snacks with chutney"></div>

    <div class="col" style="left:220px;top:154px;width:184px">
      <div>
        <div class="item-head">Seekh Kebab (6pcs) DF,GF, NF <span class="spice">MODERATE</span><span style="margin-left:8px;font-size:4px">Extra per piece $3</span><span class="price">$18</span></div>
        <p class="desc">Lamb and chicken mince mixed with exotic spices, fresh coriander grilled on skewers in tandoor oven</p>
      </div>
      <div>
        <div class="item-head">Onion Bhaji DF,GF, NF <span class="spice">MODERATE</span><i class="veg"></i></div>
        <p class="desc">Deep fried onions marinated in chickpea, rice and corn flour with exotic spices.<br>Small (5 pcs) $6 | Large (10 pcs) $10 Extra per piece $1</p>
      </div>
      <div>
        <div class="item-head">Tandoori/Tikka DF,GF, NF <span class="spice">MODERATE</span></div>
        <p class="desc">Paneer (cheese)/chicken/seafood marinated in yoghurt and exotic spices roasted in tandoor oven<br>Lemon coriander boneless chicken / Paneer (cheese) 8 pcs $14 extra per piece $1.5<br>Chicken on bone 1/2 bird $10 ; whole bird $18 Fish /Prawn 8 pcs $20 ; extra per piece $2.5</p>
      </div>
    </div>

    <div class="photo" style="left:220px;top:283px;width:184px;height:79px;background:radial-gradient(ellipse at 45% 55%,#e6c878 0%,#cfa957 35%,#7a8a3a 60%,#eeeae2 85%)" role="img" aria-label="Chaat topped with crispy noodles and herbs"></div>

    <div class="band-title">ENTRÉE PLATTERS FOR ONE PERSON - $10</div>

    <div class="col" style="left:220px;top:396px;width:184px;gap:3px">
      <div><div class="item-head">Chicken platter</div><p class="desc">One piece of each : chicken 65, lemon chicken tikka, tandoori chicken on bone and chicken samosa</p></div>
      <div><div class="item-head">Tandoori Platter</div><p class="desc">One piece of each : lemon chicken tikka, tandoori chicken on bone, Seekh kebab and paneer (cheese)</p></div>
      <div><div class="item-head">Mixed Platter</div><p class="desc">2 pieces of each : onion bhaji, Chicken 65, Lemon chicken tikka, and Gobi 65</p></div>
      <div><div class="item-head">Vegan Platter</div><p class="desc">3 pieces of each : onion bhaji, mixed pakoras and tossed veggies</p></div>
      <div><div class="item-head">Vegetarian Platter</div><p class="desc">Vegetable samosa (1 pcs), Onion bhaji (2 pcs), mixed pakora (4 pcs), Gobi 65 (2 pcs)</p></div>
      <div><div class="item-head">Samosa platter</div><p class="desc">One piece of each flavour of samosa - vegetable, chicken and lamb</p></div>
      <div><div class="item-head">Seafood platter</div><p class="desc">One piece of each : fish pakora, prawn pakora, fish tandoori and prawn tandoori</p></div>
    </div>

    <div class="page-foot"></div>
  </section>

  <section class="page page--curries">
    <div class="page-header"><div class="header-garnish" role="img" aria-label="Red chillies and a bowl of rice"></div></div>
    <div class="brand"><span class="brand-name">Mango Grove</span><span class="brand-sub">INDIAN RESTAURANT</span></div>
    <div class="section-tag" style="top:73px"><span>CURRIES</span></div>
    <div class="price-line">Veg $18 Paneer (Cheese) $20 | Chicken $22 | Lamb $24 | Seafood $25</div>

    <div class="col curry-list" style="left:17px;top:100px;width:185px">
      <div><div class="item-head">Aam (Mango) Chicken GF <span class="spice">MILD</span></div><p class="desc">Boneless chicken pieces are cooked with exotic spices, ginger and garlic and then simmered in a semi thick sauce made with onion base, nut pastes, yoghurt, cream, mango pulp and a selection of wonderful spices</p></div>
      <div><div class="item-head">Bagara Baingan (eggplant) GF, DF <span class="spice">MILD</span><i class="veg"></i></div><p class="desc">Deep fried eggplant pieces simmered in peanut, desiccated coconut, sesame seeds, cane sugar, onion-tomato masala with exotic spices</p></div>
      <div><div class="item-head">Aloo Gobi Adraki GF, DF option, NF <span class="spice">MEDIUM, HOT</span><i class="veg"></i></div><p class="desc">Deep fried cauliflower and potatoes cooked in a thick onion tomato masala with butter, yoghurt, garlic and a few exotic spices, fresh ginger and a squeeze of fresh lemon</p></div>
      <div><div class="item-head">Chole (chickpea) Masala GF, DF, NF <span class="spice">MEDIUM, MODERATE</span><i class="veg"></i></div><p class="desc">Boiled chickpeas pan fried with ginger-garlic paste and onion-tomato masala and home-made chole spice mix</p></div>
      <div><div class="item-head">Aloo Chutney Wale GF, NF <span class="spice">MODERATE</span></div><p class="desc">Cubes of boiled and fried potatoes stir-fried with mint coriander sauce made with yoghurt, young ginger, green chillies, a few exotic spices and a squeeze of fresh lemon</p></div>
      <div><div class="item-head">Chettinad GF, DF, NF <span class="spice">HOT</span><i class="veg"></i></div><p class="desc">Choice of vegetables/meats/seafood cooked in a semi thick spicy sauce made with tomatoes, onion, desiccated coconut, coconut cream, Kashmiri red chillies and exotic spices.<br>Chicken | Lamb | Paneer | Fish | Prawn | Vegetables | Potato</p></div>
      <div><div class="item-head">Dal Yellow GF, DF, NF <i class="veg"></i></div><p class="desc">Mix of lentils boiled until rich and creamy, tempered with whole spices.</p></div>
      <div><div class="item-head">Aloo Gosht (Potato with lamb) GFO <span class="spice">MODERATE</span></div><p class="desc">Diced lamb pieces are cooked with exotic spices, ginger and garlic and then simmered along with boiled potato in a thin sauce made with onion base, home-made special spice masala mix, mint, coriander, cashew nut paste, cream, yoghurt, butter, fresh garlic, fresh ginger and a wide variety of exotic spices.</p></div>
    </div>

    <div class="col curry-list" style="left:220px;top:100px;width:184px">
      <div><div class="item-head">Aloo Jeera GF, DF option, NF <span class="spice">MODERATE</span></div><p class="desc">Boiled potatoes tossed in butter with simple masalas, roasted cumin seeds, chopped ginger, garlic coriander and a squeeze of fresh lemon</p></div>
      <div><div class="item-head">Dal Makhani GF, NF <span class="spice">MILD</span></div><p class="desc">Slow cooked mix of lentils with cream, honey, tomato, dry fenugreek leaves, exotic spices tempered with whole spices</p></div>
      <div><div class="item-head">Aloo Khatte Meethe DF, NF <span class="spice">MILD</span></div><p class="desc">Cubes of boiled and fried potato stir fried with tamarind and date sauce made from young ginger, green chillies and a few exotic spices</p></div>
      <div><div class="item-head">Dal Gosht (lentils and Lamb) <span class="spice">MEDIUM, HOT</span></div><p class="desc">Diced lamb cooked with exotic spices, ginger-garlic simmered with boiled lentils, green chillies, coriander, garlic and exotic spices</p></div>
      <div><div class="item-head">Aloo Masala DF, NF <span class="spice">MEDIUM, HOT</span></div><p class="desc">Mashed potatoes pan fried in sesame oil tempered with mustard seeds, cumin seeds, fresh curry leaves, ginger, garlic and onion tomato masala</p></div>
      <div><div class="item-head">Goan style 1/, DF, NF <span class="spice">MEDIUM, HOT</span></div><p class="desc">A semi-thick sauce made with coconut cream, tamarind, turmeric, rice, fresh garlic, and various Goan spices.</p></div>
      <div><div class="item-head">Avial GF <span class="spice">MODERATE</span></div><p class="desc">A coconut based creamy vegetarian curry made with yoghurt, coconut milk and green chillies along with a variety of seasonal vegetables and a selection of exotic spices</p></div>
      <div><div class="item-head">Haandi Mixed Veg GF <span class="spice">MODERATE</span></div><p class="desc">Seasoned vegetables simmered in thick home-made onion-tomato masala with cashew nut paste, cream and exotic spices</p></div>
    </div>

    <div class="photo" style="left:18px;top:400px;width:386px;height:165px;background:linear-gradient(100deg,#d9c9a6 0%,#b3552e 25%,#e2dccf 45%,#c2742c 60%,#d9a93e 75%,#8c5e3a 100%)" role="img" aria-label="Table spread of curries, rice, breads and chutneys"></div>

    <div class="page-foot"></div>
  </section>

</div>
</body>
</html>
```